KWR CONSTRUCTION CO POSTCARD DESIGN

I was thinking of making a postcard for mailings by printmeadow and or by me dropping off at homes . I guess it would be used as a mailing post card and or flyer . I have had sketch harbor design my buisnes cards . The buisness card design is a different version from my signage on trucks because of space . I have a logo design . thyat i can upload . I like silver for back ground and black for logo and letters with glossy finish . I would like to have the KWR with a back drop to give it depth , it would be the same color as windows .

The file i submitted ha a design with red letters , this design is more detailed than the other and should be used . The colors should be black on a silver card glossy . The windows and maybe give the letters depth with a backdrop outline . I want to let home owners know that they can always call for consultation and and repairs or maintenance for their home .

Target Market(s)

home owners

Industry/Entity Type

Construction

Font styles to use
Other font styles liked:
• The same font as used in the picture of the sign i uploaded

Requirements
Must have
• HOME IMPROVEMENTS , MAINTENANCE AND REPAIRS , CARPENTRY , TILE PAINTING ECT

```html
<!DOCTYPE html>
<html lang="en">
<head>
<meta charset="utf-8">
<title>KWR Construction Co Postcard</title>
<link rel="stylesheet" href="https://fonts.googleapis.com/css2?family=Arvo:wght@400;700&display=swap">
<style>
  :root {
    --stage: #2a2a2a;
    --silver-light: #f4f4f4;
    --silver-mid: #c9c9c9;
    --silver-dark: #9a9a9a;
    --ink: #1c1c1c;
    --red: #b3161b;
    --red-dark: #7a0c10;
    --charcoal: #333333;
    --paper: #ffffff;
    --photo-sky: #a9c4d6;
    --photo-warm: #d48a3c;
    --photo-wood: #8a6a4a;
  }
  * { margin: 0; padding: 0; box-sizing: border-box; }
  html, body { width: 806px; height: 1200px; overflow: hidden; background: var(--stage); }
  body { position: relative; font-family: "Arvo", serif; }

  .postcard-front {
    position: absolute; left: 88px; top: 52px; width: 630px; height: 488px;
    background: linear-gradient(100deg, var(--silver-mid) 0%, var(--silver-light) 45%, var(--silver-mid) 75%, var(--silver-dark) 100%);
    overflow: hidden;
  }
  .postcard-front svg, .back-info svg { position: absolute; left: 0; top: 0; }

  .brand {
    position: absolute; left: 447px; top: 40px; width: 158px; text-align: center;
    color: var(--ink); font-family: "Arvo", serif; font-weight: 700;
  }
  .brand-name { font-size: 62px; line-height: 1; letter-spacing: 1px; }
  .brand-sub { font-size: 11px; letter-spacing: 1px; margin-top: 6px; }

  .services { position: absolute; left: 15px; top: 256px; color: var(--ink); }
  .services-title { font-size: 25px; font-weight: 700; letter-spacing: 1px; margin-bottom: 22px; }
  .services-list { list-style: none; }
  .services-list li {
    font-size: 18px; font-weight: 700; letter-spacing: 1px; height: 40px;
    display: flex; align-items: flex-start;
  }
  .services-list li::before {
    content: ""; width: 0; height: 0; margin: 3px 10px 0 2px;
    border-left: 17px solid var(--red); border-top: 8px solid transparent; border-bottom: 8px solid transparent;
  }

  .postcard-back {
    position: absolute; left: 92px; top: 618px; width: 621px; height: 482px;
    background: var(--paper); overflow: hidden;
  }
  .back-info {
    position: absolute; left: 0; top: 0; width: 300px; height: 482px;
    background: linear-gradient(90deg, var(--silver-mid) 0%, var(--silver-light) 55%, var(--silver-mid) 100%);
  }
  .contact { position: absolute; left: 16px; top: 236px; list-style: none; color: var(--ink); }
  .contact li { display: flex; font-size: 15px; font-weight: 700; line-height: 23px; margin-bottom: 5px; }
  .contact svg { position: static; flex: none; margin: 5px 8px 0 0; }

  .stamp-box { position: absolute; left: 498px; top: 51px; width: 83px; height: 89px; border: 1.5px solid var(--ink); }
  .address-line { position: absolute; left: 334px; width: 271px; height: 0; border-top: 1.5px solid var(--ink); }
</style>
</head>
<body>

<section class="postcard-front">
  <svg width="630" height="488" viewBox="0 0 630 488">
    <defs>
      <linearGradient id="roofPhoto" x1="0" y1="0" x2="1" y2="1">
        <stop offset="0" stop-color="var(--photo-sky)"/>
        <stop offset="0.45" stop-color="var(--photo-warm)"/>
        <stop offset="1" stop-color="var(--photo-wood)"/>
      </linearGradient>
    </defs>
    <path role="img" aria-label="Photo of a roofer in a hard hat hammering boards on a roof"
          fill="url(#roofPhoto)"
          d="M0,88 C150,45 300,70 400,150 C460,195 560,200 630,190 V400 C560,410 480,395 420,345 C330,265 200,228 0,238 Z"/>
    <path d="M0,88 C150,45 300,70 400,150 C460,195 560,200 630,190" fill="none" stroke="var(--ink)" stroke-width="8"/>
    <path d="M0,82 C150,39 300,64 400,144 C460,189 560,194 630,184" fill="none" stroke="var(--red)" stroke-width="6"/>
    <path d="M0,238 C200,228 330,265 420,345 C480,395 560,410 630,400" fill="none" stroke="var(--ink)" stroke-width="9"/>
    <path d="M0,244 C200,234 330,271 420,351 C480,401 560,416 630,406" fill="none" stroke="var(--red)" stroke-width="5"/>
    <rect x="0" y="463" width="630" height="25" fill="var(--charcoal)"/>
  </svg>

  <div class="brand">
    <div class="brand-name">KWR</div>
    <div class="brand-sub">CONSTRUCTION CO.</div>
  </div>

  <div class="services">
    <h2 class="services-title">SERVICES:</h2>
    <ul class="services-list">
      <li>HOME IMPROVEMENTS</li>
      <li>MAINTENANCE AND REPAIRS</li>
      <li>CARPENTRY</li>
      <li>TILE PAINTING Etc.</li>
    </ul>
  </div>
</section>

<section class="postcard-back">
  <div class="back-info">
    <svg width="300" height="482" viewBox="0 0 300 482">
      <defs>
        <linearGradient id="workshopPhoto" x1="0" y1="0" x2="1" y2="1">
          <stop offset="0" stop-color="#6b4a32"/>
          <stop offset="0.5" stop-color="#b08a68"/>
          <stop offset="1" stop-color="#3a2a20"/>
        </linearGradient>
        <linearGradient id="darkBase" x1="0" y1="0" x2="0" y2="1">
          <stop offset="0" stop-color="#3d3d3d"/>
          <stop offset="1" stop-color="#222222"/>
        </linearGradient>
      </defs>
      <path role="img" aria-label="Photo of a carpenter marking a wooden board with a pencil"
            fill="url(#workshopPhoto)" d="M0,0 H300 V118 C220,112 120,160 0,228 Z"/>
      <path d="M0,228 C120,160 220,112 300,118" fill="none" stroke="var(--ink)" stroke-width="10"/>
      <path d="M0,236 C120,168 220,120 300,126" fill="none" stroke="var(--red)" stroke-width="5"/>
      <path d="M0,372 C110,372 200,420 300,470 V482 H0 Z" fill="url(#darkBase)"/>
      <path d="M0,360 C110,360 200,408 300,458" fill="none" stroke="var(--red)" stroke-width="9"/>
      <path d="M0,370 C110,370 200,418 300,468" fill="none" stroke="var(--red-dark)" stroke-width="3"/>
    </svg>

    <ul class="contact">
      <li>
        <svg width="15" height="13" viewBox="0 0 15 13"><path d="M7.5,0 L15,6.5 H13 V13 H9 V9 H6 V13 H2 V6.5 H0 Z" fill="var(--red)"/></svg>
        <span>27 Alder Row<br>Milton, MA. 02186</span>
      </li>
      <li>
        <svg width="14" height="14" viewBox="0 0 14 14"><path d="M3,0 L5.5,3.5 L4,5.5 C5,7.8 6.2,9 8.5,10 L10.5,8.5 L14,11 L12,14 C6,13.5 0.5,8 0,2 Z" fill="var(--red)"/></svg>
        <span>555-014-2290</span>
      </li>
      <li>
        <svg width="12" height="12" viewBox="0 0 12 12"><circle cx="6" cy="6" r="5.2" fill="none" stroke="var(--red)" stroke-width="1.3"/><path d="M0.8,6 H11.2 M6,0.8 V11.2 M6,0.8 C3,4 3,8 6,11.2 M6,0.8 C9,4 9,8 6,11.2" fill="none" stroke="var(--red)" stroke-width="1"/></svg>
        <span>www.kwrconstructionco.com</span>
      </li>
    </ul>
  </div>

  <div class="stamp-box"></div>
  <div class="address-line" style="top:220px"></div>
  <div class="address-line" style="top:266px"></div>
  <div class="address-line" style="top:313px"></div>
</section>

</body>
</html>
```